Brochure/flyer for Tuftmoor Nappy Company

My Business name is Plover Wrenlyn Nappies
I am wanting a A4 size brochure (Flyer) to be folded twice. Measurements when folded 210 x 99 mm
I am just about to launch my Modern Cloth Nappy Products and i am wanting a brochure to target new mum's who aren't familiar with Modern cloth nappies and also for mums who are familiar with modern cloth nappies but are looking at trying my brand.
I want the Brochure to be very informative but yet Simple to read. I want people to feel like they want to buy my nappies after they read my Brochure.
The Brochure can be reworded and additional information can be added if you feel its needed, But i would like all the information listed below to be on the brochure.

MOTO: Cloth Nappies The Modern Way

The nappy design is designed in Australia and Australian Owned.

WHY USE CLOTH?
-Save thousands of Dollars
-Easy to use
-Looks Cute
-Super Absorbency
It costs approximately $3000 to use disposable nappies on a child from birth until 2 and a half years, that is Approximately 6000 nappies going into Landfill. This is based on a child going through 6-8 nappies per day.
Modern cloth nappies, on the other hand, cost around $500 for a full stash of 24 nappies. This allows for the child to wear 6-8 nappies per day with a load of nappies going in the wash every 2-3 days. As we have a range of nappies that are one-size-fits-most for bubs ranging from 3kg to 18kg, that $500 would cover your complete stash from birth right through to toilet training, Not to mention the money you would save by using the nappies again for any subsequent Children you may have.
Eliminates your baby's exposure to harmful Chemicals that can be in disposable nappies.
The manufacturing and use of disposable nappies can amount to 2-3 times more wasted water than using cloth nappies
Using Disposable Nappies fill up our landfill, Disposable nappies take more than 100 years to decompose, possibly up to 500 years.

PRODUCTS AVAILABLE:
Newborn: All in One (AIO) Fits approx 2-7kg
Velcro All in Two, One size Fits Most (OSFM) fits approx 3 to 18kg
Snap All in Two, One size Fits Most (OSFM) Fits Approx 3 to 18kg
Extra Inserts
Wetbags
Bamboo Biodegradable liners

The Materials used and features:
All in 2 Nappy (AI2):
Outer Shell Features- A waterproof TPU shell to keep all the wetness in.
Lining is a made of Microfleece material which is soft on baby's skin and Wicks moisture away from the baby's skin it is also very fast drying
Double leg Gussets to avoids any potential side leg Leaks
a poo guard at the back to reduce any leaks from occurring up the back
Insert is Made from 70% Bamboo and 30% Organic Cotton, The extra trim insert with extra absorbency qualities that can easily be double up for a heavy wetting baby or for an all night solution.

Insert snaps in and out Which is easy to remove and replace
A Pocket opening is also available to add a Booster in for long naps or for night time use. Insert is 2 layers sewn together and then folded twice to create 6 layers of absorbency. Unsnap insert from shell for washing, As there is not 3 layers sewn together like most inserts, it dries much quicker and washes more thoroughly, therefore less chance of smells accumulating

Why are these inserts so great?
– Super soft and silky
– Very breathable
– Naturally Anti-bacterial
– Absorbs 3 to 4 times more than cotton
– Doesn't feel sticky or uncomfortable when wet

The newborn nappy has a TPU waterproof Shell and is a all in one (AIO), has 4 layers of absorbency of 70% Bamboo and 30% Organic Cotton, With Microfleece lining which is super soft on newborns delicate skin.
The newborn nappy has a snap to hold down the front of the nappy where the umbilical cord will be for the first week or so. there is also snaps to adjust the size that little bit smaller for Premature babies or small babies. There is also double leg gussets to avoid any leaks around the legs. There is also a Poo guard at the back to avoid any leaks coming up from the back. The waist has a cross over snap for a extra small waist

PRICING:
One Size Fits Most:
Velcro: $25.95
Snap: $25.95
All In One Newborn:
$19.95

PACKAGES:
Price Depends on What nappies you choose for your package

Trial 3 pack: 5% Discount
6 Pack: 10% Discount
12 Pack: 15% Discount
24 Pack: 20% discount

Extra Inserts $7.00
Wetbags: $10
Bamboo Biodegradable Liners: $10
Contact Details:
Jolene Pridmore
Phone: 0491730284
E-mail: ploverwrenlynnappies@mailzenbox.com
Facebook: www.socialnookhub.com/PloverWrenlynNappies

I have changed a few things on the brief so please read carefully before changing or making another design,

Thanks :) 

Target Market(s)

Mums and Dads, care takers, Guardians and grandparents

Industry/Entity Type

Baby

Requirements
Must have
• Must have the Logo and picture i have sent but you are welcome to put other pictures of babies but please do not put pictures of babies with disposable nappies on. and if you are going to put pics of babies i would prefer the pictures not to show how the Velcro or snaps look at the front of the nappy. for example: put pictures that show the nappy side on or from the back. You could put pictures of babies or of nature etc "saving the Environment"
Should not have
• no pictures of other cloth nappy brands No disposable nappies

```html
<!DOCTYPE html>
<html lang="en">
<head>
<meta charset="utf-8">
<title>Plover Wrenlyn Nappies – Trifold Brochure</title>
<link href="https://fonts.googleapis.com/css2?family=Gabriela&family=Alegreya:ital@0;1&family=Parisienne&display=swap" rel="stylesheet">
<style>
  :root{
    --stage:#0d0d0d;
    --purple:#7c3f99;
    --purple-deep:#5b2b7a;
    --purple-soft:#a86cc0;
    --lilac:#d7b3e2;
    --blush:#f3e3f3;
    --white:#ffffff;
    --ink-script:#8a3fa0;
    --name-script:#6a3a86;
  }
  *{box-sizing:border-box;margin:0;padding:0}
  html,body{width:1200px;height:673px;overflow:hidden;background:var(--stage)}
  .brochure{position:absolute;left:161px;top:26px;width:877px;height:620px;display:flex}
  .panel{position:relative;width:292.33px;height:620px;overflow:hidden}

  /* Panel 1: packages */
  .panel--packages{background:var(--purple)}
  .product-photo{position:absolute;left:0;top:0;width:100%;height:250px;
    background:linear-gradient(135deg,#7fc3e3 0%,#f2eec0 30%,#e43a3a 55%,#9bd49a 75%,#2f5fa8 100%)}
  .wave{position:absolute;left:0;top:205px;width:100%;height:80px}
  .packages-title{position:absolute;top:300px;width:100%;text-align:center;
    font-family:"Gabriela",serif;font-size:30px;color:var(--white);letter-spacing:1px}
  .packages-intro{position:absolute;top:344px;left:14px;right:14px;text-align:center;
    font-family:"Alegreya",serif;font-size:17px;line-height:1.3;color:var(--white)}
  .package-list,.extras-list{position:absolute;left:0;width:100%;list-style:none;text-align:center;
    font-family:"Alegreya",serif;font-size:15px;line-height:1.38;color:var(--white)}
  .package-list{top:410px}
  .extras-list{top:530px}

  /* Panel 2: why cloth & pricing */
  .panel--why{background:linear-gradient(90deg,var(--purple) 0%,var(--purple) 75%,var(--purple-deep) 100%)}
  .why-label{position:absolute;left:22px;top:16px;width:170px;height:30px;border-radius:15px;
    background:var(--white);font-family:"Gabriela",serif;font-style:italic;font-size:15px;
    color:var(--purple);line-height:30px;padding-left:14px}
  .why-label .dot{position:absolute;right:-12px;top:1px;width:28px;height:28px;border-radius:50%;
    background:var(--purple-soft);border:2px solid var(--white)}
  .benefit-list{position:absolute;left:22px;top:56px;list-style:none;
    font-family:"Alegreya",serif;font-size:14px;line-height:1.35;color:var(--white)}
  .benefit-list li{position:relative;padding-left:18px}
  .benefit-list li::before{content:"";position:absolute;left:0;top:5px;width:11px;height:11px;border-radius:50%;
    background:var(--lilac);border:2px solid var(--purple-soft)}
  .why-copy{position:absolute;left:22px;right:18px;top:140px;font-family:"Alegreya",serif;
    font-size:8px;line-height:1.42;color:var(--white)}
  .why-copy p{margin-bottom:8px}
  .pricing-box{position:absolute;left:10px;top:440px;width:246px;height:152px;border:2px solid var(--white);
    border-radius:10px;text-align:center;color:var(--white)}
  .pricing-box .corner{position:absolute;width:30px;height:30px;border-radius:50%;background:var(--purple-soft);border:2px solid var(--white)}
  .pricing-box .corner--top{left:-8px;top:-16px}
  .pricing-box .corner--bottom{right:-10px;bottom:-14px}
  .pricing-title{margin-top:10px;font-family:"Gabriela",serif;font-size:28px;letter-spacing:1px}
  .pricing-sub{font-family:"Alegreya",serif;font-size:16px;margin-top:-2px}
  .price-list{list-style:none;margin-top:8px;font-family:"Alegreya",serif;font-size:14.5px;line-height:1.42}

  /* Panel 3: cover */
  .panel--cover{background:linear-gradient(180deg,var(--white) 0%,var(--blush) 100%)}
  .brand-mark{position:absolute;left:22px;top:22px;width:84px;height:84px;border-radius:50%;background:var(--purple-soft)}
  .brand-name{position:absolute;left:24px;top:132px;font-family:"Parisienne",cursive;font-size:24px;color:var(--name-script)}
  .motto{position:absolute;left:22px;top:178px;font-family:"Parisienne",cursive;font-size:38px;line-height:1.2;color:var(--ink-script)}
  .baby-photo{position:absolute;left:0;top:330px;width:100%;height:290px;
    background:linear-gradient(180deg,#6b4a3a 0%,#e8c3b3 35%,#f2d3c6 70%,#f5b4cc 100%)}
  .cover-band{position:absolute;left:0;top:288px;width:100%;height:110px}
</style>
</head>
<body>
<main class="brochure">

  <section class="panel panel--packages">
    <div class="product-photo" role="img" aria-label="Stack of colourful modern cloth nappies in blue, cream, green, red and navy"></div>
    <svg class="wave" viewBox="0 0 292 80" preserveAspectRatio="none" aria-hidden="true">
      <path d="M0 40 C40 22 70 30 95 48 C120 30 160 18 200 30 C235 40 262 26 292 10 L292 80 L0 80 Z" fill="#a86cc0"/>
      <path d="M0 56 C45 40 75 46 98 62 C125 46 165 36 205 46 C240 54 265 42 292 30 L292 80 L0 80 Z" fill="#7c3f99"/>
    </svg>
    <h2 class="packages-title">PACKAGES</h2>
    <p class="packages-intro">Price Depends on What nappies you choose for your package</p>
    <ul class="package-list">
      <li>Trial 3 pack: 5% Discount</li>
      <li>6 Pack: 10% Discount</li>
      <li>12 Pack: 15% Discount</li>
      <li>24 Pack: 20% discount</li>
    </ul>
    <ul class="extras-list">
      <li>Extra Inserts $7.00</li>
      <li>Wetbags: $10</li>
      <li>Bamboo Biodegradable Liners: $10</li>
    </ul>
  </section>

  <section class="panel panel--why">
    <h2 class="why-label">Why Use Cloth?<span class="dot"></span></h2>
    <ul class="benefit-list">
      <li>Save thousands of Dollars</li>
      <li>Easy to use</li>
      <li>Looks Cute</li>
      <li>Super Absorbency</li>
    </ul>
    <div class="why-copy">
      <p>It costs approximately $3000 to use disposable nappies on a child from birth until 2 and a half years, that is Approximately 6000 nappies going into Landfill. This is based on a child going through 6-8 nappies per day.</p>
      <p>Modern cloth nappies, on the other hand, cost around $500 for a full stash of 24 nappies. This allows for the child to wear 6-8 nappies per day with a load of nappies going in the wash every 2-3 days. As we have a range of nappies that are one-size-fits-most for bubs ranging from 3kg to 18kg, that $500 would cover your complete stash from birth right through to toilet training. Not to mention the money you would save by using the nappies again for any subsequent Children you may have. Eliminates your baby's exposure to harmful Chemicals that can be in disposable nappies.</p>
      <p>The manufacturing and use of disposable nappies can amount to 2-3 times more wasted water than using cloth nappies</p>
      <p>Using Disposable Nappies fill up our landfill, Disposable nappies take more than 100 years to decompose, possibly up to 500 years.</p>
    </div>
    <div class="pricing-box">
      <span class="corner corner--top"></span>
      <h2 class="pricing-title">PRICING</h2>
      <p class="pricing-sub">One Size Fits Most</p>
      <ul class="price-list">
        <li>Velcro: $25.95</li>
        <li>Snap: $25.95</li>
        <li>All In One Newborn:$19.95</li>
      </ul>
      <span class="corner corner--bottom"></span>
    </div>
  </section>

  <section class="panel panel--cover">
    <span class="brand-mark" aria-hidden="true"></span>
    <p class="brand-name">Plover Wrenlyn</p>
    <h1 class="motto">Cloth Nappies<br>The Modern Way</h1>
    <div class="baby-photo" role="img" aria-label="Portrait photo of a smiling baby"></div>
    <svg class="cover-band" viewBox="0 0 292 110" preserveAspectRatio="none" aria-hidden="true">
      <path d="M0 40 C40 36 60 40 80 52 C110 10 190 4 225 48 C250 70 270 70 292 62 L292 82 C270 90 248 88 225 70 C190 30 112 34 80 72 C60 58 30 54 0 58 Z" fill="#7c3f99"/>
      <path d="M0 58 C30 54 60 58 80 72 C112 34 190 30 225 70 C248 88 270 90 292 82 L292 92 C268 100 245 96 225 80 C190 46 115 50 80 84 C58 70 30 66 0 70 Z" fill="#b98ccb"/>
    </svg>
  </section>

</main>
</body>
</html>
```